書籍の表紙デザインをしていただける方をコンペにて募集いたします。 現在認知症予防になる生活習慣を書籍を制作しております。 こちらにある書籍のような、マンガと解説を組み合わせた構成になる予定です。 https://www.torimaru-shoten.jp/bk/4/2860/7/ 制作いただきたいのは表紙デザイン1点となります。 こちらも上記ページにあるもののように、イラスト+文字の表紙にしていただきたく思います。 帯の部分もアリの形でお願いします。 サイズはA5を予定しております。 メインターゲットは60代くらいの女性となります。 使用していただきたいイラストは添付しております。 以下が文言となります。 ↓ マンガでわかる 医学博士がすすめる 朝の散歩で若返る毎日の工夫 ← タイトル 初期認知症患者の9割が改善!? 世界で話題の予防・治療法が わかる! 実践できる! 執筆: 堀内達郎 作画: 菅野 渉 一般社団法人はつらつ会議 ←ロゴ ・契約金額 : 3万円(税込) ご質問等あればお気軽にお送りください。 ご応募お待ちしております。 |
もっともバランスがよく、目を引くデザインだと感じましたので採用させていただきました。
たくさんの素敵なご提案ありがとうございました。ひとつに絞らなければならないのが大変心苦しく感じました。また機会がありましたらよろしくお願いいたします。

```html
<!DOCTYPE html>
<html lang="ja">
<head>
<meta charset="UTF-8">
<title>朝の散歩で若返る毎日の工夫 — 表紙</title>
<link rel="stylesheet" href="https://fonts.googleapis.com/css2?family=Noto+Sans+JP:wght@500;700;900&family=Shippori+Mincho+B1:wght@800&display=swap">
<style>
  :root {
    --paper: #ffffff;
    --ink: #161616;
    --accent-green: #4f9a2c;
    --band-green: #d3e89c;
    --band-green-deep: #bcd97a;
    --band-text: #2d6a1a;
    --skin: #f2d9c6;
    --hair: #8a5a3c;
    --shirt: #3f4a72;
    --blouse: #e9e6ee;
  }
  * { margin: 0; padding: 0; box-sizing: border-box; }
  html, body { width: 845px; height: 1200px; overflow: hidden; background: var(--paper); }
  .cover {
    position: relative;
    width: 845px;
    height: 1200px;
    background: var(--paper);
    font-family: "Noto Sans JP", sans-serif;
    color: var(--ink);
    overflow: hidden;
  }
  .cover-art {
    position: absolute;
    left: 0;
    top: 0;
    width: 640px;
    height: 900px;
    background:
      radial-gradient(ellipse 150px 130px at 250px 150px, var(--hair) 0%, rgba(138,90,60,0) 100%),
      radial-gradient(ellipse 130px 150px at 270px 270px, var(--skin) 0%, rgba(242,217,198,0) 100%),
      radial-gradient(ellipse 200px 210px at 220px 560px, var(--skin) 0%, rgba(242,217,198,0) 100%),
      radial-gradient(ellipse 240px 200px at 420px 470px, var(--shirt) 0%, rgba(63,74,114,0) 100%),
      radial-gradient(ellipse 300px 200px at 240px 800px, var(--blouse) 0%, rgba(233,230,238,0) 100%),
      radial-gradient(ellipse 330px 460px at 270px 420px, #f6e7dc 0%, rgba(255,255,255,0) 100%);
  }
  .endorsement {
    position: absolute;
    top: 22px;
    right: 60px;
    font-size: 46px;
    font-weight: 900;
    letter-spacing: 0.02em;
    line-height: 1;
  }
  .title {
    position: absolute;
    top: 92px;
    right: 14px;
    text-align: right;
    font-family: "Shippori Mincho B1", serif;
    font-weight: 800;
    line-height: 1.42;
  }
  .title-line { display: block; }
  .title-line--wide { font-size: 112px; }
  .title-line--short { font-size: 140px; }
  .series-label {
    position: absolute;
    top: 640px;
    right: 52px;
    font-size: 28px;
    font-weight: 700;
    color: var(--ink);
    letter-spacing: 0.04em;
    border-bottom: 3px solid var(--accent-green);
    padding-bottom: 2px;
  }
  .credits {
    position: absolute;
    top: 896px;
    left: 228px;
    display: flex;
    gap: 40px;
    font-size: 30px;
    font-weight: 500;
  }
  .obi {
    position: absolute;
    left: 0;
    bottom: 0;
    width: 845px;
    height: 240px;
    background: linear-gradient(180deg, var(--band-green-deep) 0%, var(--band-green) 25%, var(--band-green) 100%);
  }
  .obi-copy {
    position: absolute;
    left: 18px;
    top: 16px;
    color: var(--band-text);
    font-weight: 900;
  }
  .obi-copy p { line-height: 1.36; }
  .obi-lead { font-size: 46px; }
  .obi-sub { font-size: 46px; }
  .obi-call { font-size: 62px; }
  .publisher {
    position: absolute;
    right: 22px;
    bottom: 28px;
    display: flex;
    align-items: center;
    gap: 10px;
    font-size: 24px;
    font-weight: 700;
    color: var(--band-text);
  }
  .publisher-mark {
    width: 36px;
    height: 36px;
    border-radius: 50%;
    background: var(--band-text);
  }
</style>
</head>
<body>
  <main class="cover">
    <div class="cover-art" role="img" aria-label="マンガ調のイラスト：笑顔の高齢女性の肩に手を置く若い女性"></div>

    <p class="endorsement">医学博士がすすめる</p>

    <h1 class="title">
      <span class="title-line title-line--wide">朝の散歩で</span>
      <span class="title-line title-line--short">若返る</span>
      <span class="title-line title-line--wide">毎日の工夫</span>
    </h1>

    <p class="series-label">マンガでわかる</p>

    <p class="credits">
      <span>執筆: 堀内達郎</span>
      <span>作画: 菅野 渉</span>
    </p>

    <section class="obi">
      <div class="obi-copy">
        <p class="obi-lead">初期認知症患者の9割が改善!?</p>
        <p class="obi-sub">世界で話題の予防・治療法がわかる!</p>
        <p class="obi-call">実践できる!</p>
      </div>
      <div class="publisher">
        <span class="publisher-mark"></span>
        <span>一般社団法人はつらつ会議</span>
      </div>
    </section>
  </main>
</body>
</html>
```